Clean Plinth Ads Banner Design For A Finance Company

Hi,
We're a UK based finance company and are looking for new banner ads to use on the Plinth Display Network.
We want the end product to stand out by using strong, minimal design - ideally starting from a dark theme, although I'm open to ideas.
The copy should read:
'Fast Bridging Loans From 0.39% PM'
Once we have these designs agreed, we are looking to replicate them for other products, changing only the text on each ad - for example, 'commercial mortgage service you can rely on' or 'development finance service you can rely on'.
The colours used on our website are the following:
Black - #040303
Orange - #f79124
White - #ffffff
Grey - #ffffff
Example ads that I like - https://www.brimcastle.com/wp-content/uploads/2021/07/plinth-display-ads-example-2-final.png.webp
2 - https://quendrahub.com/wp-content/uploads/2020/03/fbdd56ba3bd16c7a8debb13a411de786.jpg

```html
<!DOCTYPE html>
<html lang="en">
<head>
<meta charset="utf-8">
<title>Orvane Finance – Bridging Loan Service Banner</title>
<link rel="stylesheet" href="https://fonts.googleapis.com/css2?family=Barlow:wght@400;500;600;700&display=swap">
<style>
  :root {
    --black: #040303;
    --orange: #f79124;
    --white: #ffffff;
    --shadow: #8a8a8a;
    --photo-warm-light: #f0cfae;
    --photo-warm-mid: #c98a4f;
    --photo-warm-dark: #6b4326;
  }
  html, body {
    margin: 0;
    padding: 0;
    width: 1200px;
    height: 1200px;
    overflow: hidden;
    background: var(--white);
  }
  .canvas {
    position: relative;
    width: 1200px;
    height: 1200px;
    font-family: "Barlow", sans-serif;
  }
  .banner-shadow {
    position: absolute;
    left: 120px;
    top: 337px;
    width: 989px;
    height: 552px;
    background: var(--shadow);
  }
  .banner {
    position: absolute;
    left: 105px;
    top: 324px;
    width: 998px;
    height: 560px;
    background: var(--black);
    overflow: hidden;
  }
  .banner-art {
    position: absolute;
    inset: 0;
    width: 100%;
    height: 100%;
    display: block;
  }
  .brand {
    position: absolute;
    left: 652px;
    top: 74px;
    width: 300px;
    text-align: center;
    white-space: nowrap;
    color: var(--orange);
    font-weight: 600;
    font-size: 21px;
    line-height: 24px;
    letter-spacing: 0.3px;
  }
  .headline {
    margin: 0;
    font-size: inherit;
    font-weight: inherit;
  }
  .headline span {
    position: absolute;
    left: 674px;
    display: block;
    white-space: nowrap;
    line-height: 1;
  }
  .headline-top {
    top: 133px;
    font-size: 43px;
    font-weight: 400;
    letter-spacing: 12.5px;
    color: var(--white);
  }
  .headline-main {
    top: 167px;
    font-size: 106px;
    font-weight: 600;
    letter-spacing: 0;
    color: var(--white);
  }
  .headline-accent {
    top: 266px;
    font-size: 66px;
    font-weight: 700;
    letter-spacing: 0.5px;
    color: var(--orange);
  }
  .tagline {
    position: absolute;
    left: 675px;
    top: 335px;
    margin: 0;
    white-space: nowrap;
    color: var(--white);
    font-size: 26px;
    font-weight: 400;
    line-height: 30px;
    letter-spacing: 0.4px;
  }
  .cta {
    position: absolute;
    left: 723px;
    top: 421px;
    width: 158px;
    height: 47px;
    background: var(--orange);
    color: var(--white);
    font-size: 20px;
    font-weight: 500;
    display: flex;
    align-items: center;
    justify-content: center;
    text-decoration: none;
  }
</style>
</head>
<body>
<div class="canvas">
  <div class="banner-shadow"></div>
  <section class="banner">
    <svg class="banner-art" viewBox="0 0 1596 896" preserveAspectRatio="none">
      <defs>
        <linearGradient id="photoTeam" x1="0" y1="0" x2="1" y2="1">
          <stop offset="0" stop-color="#f0cfae"/>
          <stop offset="0.6" stop-color="#c98a4f"/>
          <stop offset="1" stop-color="#6b4326"/>
        </linearGradient>
        <linearGradient id="photoAdvisor" x1="0" y1="1" x2="1" y2="0">
          <stop offset="0" stop-color="#6b4326"/>
          <stop offset="0.5" stop-color="#c98a4f"/>
          <stop offset="1" stop-color="#f0cfae"/>
        </linearGradient>
      </defs>
      <polygon class="photo-team" points="0,0 629,0 772,147 140,787 0,662" fill="url(#photoTeam)"
        role="img" aria-label="Photo: business team in a meeting, one colleague presenting at a flip chart"/>
      <polygon class="photo-advisor" points="613,388 1122,896 102,896" fill="url(#photoAdvisor)"
        role="img" aria-label="Photo: finance advisor and client talking over a tablet in an office"/>
      <polygon class="accent-corner-left" points="0,722 107,827 37,896 0,896" fill="#f79124"/>
      <polygon class="accent-stripe-top" points="869,0 917,0 852,66 804,66" fill="#f79124"/>
      <rect class="accent-square" x="1535" y="0" width="61" height="61" fill="#f79124"/>
      <polygon class="accent-corner-right" points="1462,817 1539,896 1491,896 1462,867" fill="#f79124"/>
    </svg>

    <div class="brand">Orvane Finance Limited</div>

    <h1 class="headline">
      <span class="headline-top">BRIDGING</span>
      <span class="headline-main">LOAN</span>
      <span class="headline-accent">SERVICE</span>
    </h1>

    <p class="tagline">You Can Rely On<br>Think Orvane Finance</p>

    <a class="cta" href="#">Learn More</a>
  </section>
</div>
</body>
</html>
```